VELOR Capital Partners Presentation (around 10 pages) and web design

I need a document that present my company that I can send to my prospect, client and financial partners...and the web design that goes with it.
Our company is investing in gold mines in Africa and South America but provides as well mining operational solutions and consulting in finance and restructuring for the mining industry. the last vertical business of our company is a subsidiary "Tresvin Group" that provides logistics solutions for mining companies. the logo of Velor Capital partners, the logo and the presentation of Tresvin group have already been made by PIXELHARBOR and you will find them in the files uploaded

```html
<!DOCTYPE html>
<html lang="en">
<head>
<meta charset="utf-8">
<title>VELOR Capital Partners — Presentation Pages</title>
<link href="https://fonts.googleapis.com/css2?family=Roboto:wght@400;500;700&display=swap" rel="stylesheet">
<style>
:root{
  --brand-blue:#1ca2e1;
  --ink:#111111;
  --ink-soft:#333333;
  --paper:#ffffff;
  --paper-grey:#f3f3f3;
  --divider-grey:#cfcfcf;
  --photo-dark:#6c7a84;
  --photo-light:#c9d2d8;
  --bg-violet:#c8baff;
  --bg-pale:#f4fbff;
}
*{margin:0;padding:0;box-sizing:border-box}
html,body{width:1200px;height:800px;overflow:hidden}
body{
  font-family:"Roboto",Arial,sans-serif;
  background:radial-gradient(ellipse 70% 75% at 50% 100%,var(--bg-pale) 0%,#dce6ff 45%,var(--bg-violet) 100%);
  position:relative;
}
.slide{position:absolute;width:480px;height:270px;overflow:hidden;background:var(--paper)}
.slide--cover{left:61px;top:108px;background:radial-gradient(circle at 50% 50%,#ffffff 0%,var(--paper-grey) 100%);display:flex;align-items:center;justify-content:center}
.slide--mission{left:660px;top:108px;background:var(--brand-blue)}
.slide--value{left:61px;top:447px}
.slide--principles{left:660px;top:447px}

.brand-name{display:flex;align-items:center;gap:7px;font-size:17px;font-weight:500;color:#1e2a36;letter-spacing:.5px}
.brand-mark{width:12px;height:12px;background:var(--brand-blue)}

.mission-photo{position:absolute;left:0;top:0;width:185px;height:270px;background:linear-gradient(160deg,var(--photo-light) 0%,#9aa7b0 45%,var(--photo-dark) 100%)}
.mission-gap{position:absolute;left:185px;top:0;width:4px;height:270px;background:#a9b2b8}
.mission-title{position:absolute;left:221px;top:36px;color:var(--paper);font-size:14.5px;font-weight:700}
.rule{display:block;width:50px;height:1.5px;background:var(--paper);margin-top:5px}
.quote-icon{position:absolute;left:220px;top:85px}
.mission-text{position:absolute;left:221px;top:114px;width:232px;color:var(--paper);font-size:9.4px;line-height:13px}

.value-band{position:absolute;left:0;top:0}
.value-title{position:absolute;left:0;right:0;top:24px;text-align:center;color:var(--paper);font-size:14.5px;font-weight:700}
.value-title .rule{margin:5px auto 0}
.value-text{position:absolute;left:60px;right:60px;top:63px;text-align:center;color:var(--paper);font-size:9.2px;line-height:10.8px}
.value-tagline{position:absolute;left:0;right:0;top:178px;text-align:center;color:var(--brand-blue);font-size:15px;font-weight:700}
.value-sub{position:absolute;left:0;right:0;top:214px;text-align:center;color:var(--ink-soft);font-size:9.2px}

.principles-bar{position:absolute;left:0;top:0;width:80px;height:270px;background:var(--brand-blue)}
.principles-gap{position:absolute;left:80px;top:0;width:3px;height:270px;background:#e2e2e2}
.principles-title{position:absolute;left:109px;top:17px;color:var(--brand-blue);font-size:15px;font-weight:700}
.principle{position:absolute;width:150px}
.principle h3{color:var(--brand-blue);font-size:9px;font-weight:700;margin-bottom:7px}
.principle p{color:var(--ink);font-size:7.6px;line-height:11.2px;font-weight:500}
</style>
</head>
<body>

<section class="slide slide--cover">
  <div class="brand-name"><span class="brand-mark"></span>VELOR Capital Partners</div>
</section>

<section class="slide slide--mission">
  <div class="mission-photo" role="img" aria-label="Photograph of a gold bar resting on gravel, toned in blue-grey"></div>
  <div class="mission-gap"></div>
  <h2 class="mission-title">OUR MISSION<span class="rule"></span></h2>
  <svg class="quote-icon" width="26" height="20" viewBox="0 0 26 20" fill="none" stroke="#ffffff" stroke-width="1.4">
    <path d="M1 1h9v9l-4 9H2l3-8H1z"/>
    <path d="M15 1h9v9l-4 9h-4l3-8h-4z"/>
  </svg>
  <p class="mission-text">Our mission is to responsibly discover, develop, and operate high-quality gold mining assets that deliver sustainable value for our shareholders, employees, communities, and the environment. We are committed to operational excellence, ethical business practices, and long-term growth through strategic investment, innovation, and the development of world-class mining projects.</p>
</section>

<section class="slide slide--value">
  <svg class="value-band" width="480" height="152" viewBox="0 0 480 152">
    <polygon points="0,118 240,151 480,118 480,122 240,152 0,122" fill="#d6d6d6"/>
    <polygon points="0,0 480,0 480,118 240,148 0,118" fill="#1ca2e1"/>
  </svg>
  <h2 class="value-title">OUR VALUE<span class="rule"></span></h2>
  <p class="value-text">We are committed to safe and responsible mining that creates enduring value. Guided by integrity, we operate with excellence, protect the environment, and invest in the communities where we work. We respect our people, foster innovation, and pursue sustainable growth to benefit our shareholders, partners, and future generations.</p>
  <p class="value-tagline">Safe. Responsible. Innovative.</p>
  <p class="value-sub">We mine with integrity, protect our world, and create lasting value for all</p>
</section>

<section class="slide slide--principles">
  <div class="principles-bar"></div>
  <div class="principles-gap"></div>
  <h2 class="principles-title">Our Core Principles:</h2>
  <div class="principle" style="left:109px;top:56px"><h3>Safety First</h3><p>Protecting our people and communities above all else</p></div>
  <div class="principle" style="left:109px;top:107px"><h3>Integrity</h3><p>Acting with transparency, ethics, and accountability</p></div>
  <div class="principle" style="left:109px;top:158px"><h3>Operational Excellence</h3><p>Driving efficiency, innovation, and quality in every project</p></div>
  <div class="principle" style="left:109px;top:209px"><h3>Sustainability</h3><p>Minimizing environmental impact and managing resources responsibly.</p></div>
  <div class="principle" style="left:302px;top:56px"><h3>Community Partnership</h3><p>Building strong, respectful, and mutually beneficial relationships</p></div>
  <div class="principle" style="left:302px;top:107px"><h3>Respect for People</h3><p>Valuing diversity, fairness, and inclusion</p></div>
  <div class="principle" style="left:302px;top:158px;width:160px"><h3>Long-Term Value</h3><p>Creating enduring economic and social benefits for all stakeholders</p></div>
</section>

</body>
</html>
```